Marlow & Tate
Business card and stationery design for a management consulting firm  - Consulting
Simple
Benedikt Owen Dolsquin
Lead Consultant
Njegoševa 47 11000 Belgrade
benedikt.owen@marlowtate-example.com
www.marlowtate-example.com
Keep the design clean. "Scandinavian design approach". Address line on business card is preferred not to be included, although if designer finds it to complete the holistic 'picture' of the card, then he/she may use it. Font selection for the rest of the text is up to the designer. Although please note that the font has to be in balance with the logo. Business cards are to be printed on black paper / metal. If printed on paper, the logo part will be with relief printing.
This is designers choice to be creative
dolsquin dolsquin
Tip to designers: Try not to use the monogram "MT" with "Marlow and Tate" on the same side. Printing techniques that will be used are: Embossing / Debossing, Thermography. Keep it clean. Less is more.

```html
<!DOCTYPE html>
<html lang="en">
<head>
<meta charset="utf-8">
<title>Marlow and Tate – Business Card</title>
<link href="https://fonts.googleapis.com/css2?family=Open+Sans:wght@400;700&display=swap" rel="stylesheet">
<style>
  :root {
    --page-bg: #e6e6e4;
    --card-grey: #a9a9a9;
    --card-black: #262425;
    --ink-dark: #1c1c1c;
    --ink-light: #f2f2f2;
    --ink-muted: #cfcfcf;
    --swoosh-white: #ffffff;
    --swoosh-grey: #8c8c8c;
  }
  * { box-sizing: border-box; margin: 0; padding: 0; }
  html, body {
    width: 1200px; height: 901px; overflow: hidden;
    background: var(--page-bg);
    font-family: "Open Sans", Arial, sans-serif;
  }
  .card {
    position: absolute; left: 280px;
    width: 640px; height: 380px;
    border-radius: 4px;
    box-shadow: 0 6px 18px rgba(0,0,0,0.18);
    overflow: hidden;
  }
  .card--back { top: 40px; background: var(--card-grey); }
  .card--front { top: 480px; background: var(--card-black); color: var(--ink-light); }

  .brand-name {
    position: absolute;
    font-weight: 400;
    white-space: nowrap;
  }
  .card--back .brand-name {
    left: 0; right: 0; top: 160px; text-align: center;
    font-size: 44px; letter-spacing: 1px; color: var(--ink-dark);
  }
  .card--front .brand-name {
    left: 390px; top: 175px;
    font-size: 28px; letter-spacing: 0.5px; color: var(--ink-muted);
  }

  .holder { position: absolute; left: 36px; top: 40px; }
  .holder__name { font-weight: 700; font-size: 17px; line-height: 1.3; }
  .holder__title { font-size: 14px; color: var(--ink-muted); }

  .contact {
    position: absolute; left: 36px; top: 150px;
    font-size: 14px; line-height: 1.45; color: var(--ink-muted);
    list-style: none;
  }
  .contact__gap { height: 12px; }

  .swoosh { position: absolute; left: 0; bottom: 0; width: 640px; height: 170px; }
</style>
</head>
<body>
  <section class="card card--back" aria-label="Card back">
    <p class="brand-name">Marlow and Tate</p>
  </section>

  <section class="card card--front" aria-label="Card front">
    <div class="holder">
      <p class="holder__name">Benedikt Owen Dolsquin</p>
      <p class="holder__title">Lead Consultant</p>
    </div>
    <ul class="contact">
      <li>Njegoševa 47</li>
      <li>11000 Belgrade</li>
      <li class="contact__gap"></li>
      <li>Cell: +381 600 555 014</li>
      <li>Email: benedikt.owen@marlowtate-example.com</li>
      <li>www.marlowtate-example.com</li>
    </ul>
    <p class="brand-name">Marlow and Tate</p>
    <svg class="swoosh" viewBox="0 0 640 170" preserveAspectRatio="none" aria-hidden="true">
      <path d="M0 60 C 120 130, 320 150, 640 118 L640 170 L0 170 Z" fill="var(--swoosh-grey)"/>
      <path d="M0 40 C 90 120, 260 150, 470 170 L0 170 Z" fill="var(--swoosh-white)"/>
      <path d="M120 88 C 260 118, 420 128, 640 112 L640 116 C 420 134, 260 126, 120 88 Z" fill="var(--swoosh-white)"/>
    </svg>
  </section>
</body>
</html>
```